Website Design for Law Firm

We need a fresh new website design for our client 'Vendrick Legal' who specialises as a Criminal, Traffic & Civil Lawyer in Perth, Western Australia. We are looking for a very clean, professional and elegant look for the website, a presence of power and class needed as he deals with high end clients. Black, Silver and hints of gold need to run through the design without making the site look too dark. We are after a very modern, spacious web look, use of large readable text with links to social media (such as Chatterloom, Zumbly+, Quibbr, WorkMesh) to stand out and his contact details to be made very predominate.

Reason: Public holidays here in Australia, need more business hours to discuss designs with client.

Reason: Client needs more time to look through designs.

Reason: Client is going over last of designs. Design will be picked early next week!

Industry/Entity Type

Law Firm

```html
<!DOCTYPE html>
<html lang="en">
<head>
<meta charset="utf-8">
<title>Vendrick Legal – Criminal, Traffic &amp; Civil Lawyer, Perth WA</title>
<link rel="stylesheet" href="https://fonts.googleapis.com/css2?family=Philosopher:wght@400;700&family=Cinzel:wght@400;600&family=Arimo:wght@400;700&family=Roboto+Slab:wght@400&display=swap">
<style>
:root{
  --ink:#1d1d1d;
  --text:#4a4a4a;
  --muted:#6b6b6b;
  --gold:#c06a1f;
  --gold-light:#f0b23c;
  --gold-dark:#b4731a;
  --silver:#e9e9e9;
  --silver-mid:#cfcfcf;
  --band:#8e8e8e;
  --panel:#f3f3f3;
  --white:#ffffff;
  --black:#0e0e0e;
  --footer-bar:#5c5c5c;
}
*{box-sizing:border-box;margin:0;padding:0}
html,body{width:892px;height:1200px;overflow:hidden}
body{position:relative;background:var(--silver-mid);font-family:"Arimo",Arial,sans-serif;color:var(--text)}
a{color:var(--gold);text-decoration:none;border-bottom:1px solid var(--gold)}

.site-header{position:absolute;left:0;top:0;width:892px;height:158px;border-top:4px solid #4a4a4a;background:linear-gradient(#f6f6f6,#e4e4e4)}
.brand{position:absolute;left:88px;top:30px;display:flex;align-items:center;gap:8px}
.brand-mark{width:22px;height:22px;background:var(--ink)}
.brand-name{font-family:"Cinzel",serif;font-weight:600;font-size:26px;color:var(--ink);letter-spacing:1px}
.contact-block{position:absolute;right:88px;top:22px;text-align:right;font-family:"Cinzel",serif;color:var(--ink)}
.contact-call{font-size:12.5px;letter-spacing:1px;border-bottom:1px solid var(--ink);padding-bottom:2px}
.contact-phone{font-size:17px;margin-top:6px;letter-spacing:1px}
.contact-email{display:inline-block;margin-top:5px;background:var(--ink);color:var(--white);font-size:9.5px;padding:2px 6px;letter-spacing:1px}
.main-nav{position:absolute;left:93px;top:110px;width:711px;display:flex;justify-content:space-between;font-size:11px;color:#333}
.main-nav .current{color:var(--black);font-weight:700}
.main-nav .active{color:var(--gold)}

.hero-band{position:absolute;left:0;top:158px;width:892px;height:247px;background:linear-gradient(#6e6e6e,#b2b2b2);border-bottom:2px solid #2a2a2a}
.hero{position:absolute;left:90px;top:133px;width:718px;height:226px;background:linear-gradient(100deg,#2a1a10 0%,#5b3a1c 30%,#3b2616 55%,#1f140c 100%);box-shadow:0 6px 14px rgba(0,0,0,.35)}
.hero-title{position:absolute;left:14px;top:118px;font-family:"Arimo",sans-serif;font-weight:700;font-size:21px;color:var(--white)}
.hero-copy{position:absolute;left:14px;top:146px;width:320px;font-size:10px;line-height:14px;color:var(--white)}
.hero-button{position:absolute;left:12px;top:182px;width:118px;height:30px;border:2px solid #bdbdbd;background:linear-gradient(#efefef,#bdbdbd);font-weight:700;font-size:13px;color:#333;display:flex;align-items:center;justify-content:center}
.hero-pager{position:absolute;left:380px;top:380px;width:135px;height:25px;background:#3a3a3a;border-radius:12px 12px 0 0;display:flex;gap:9px;justify-content:center;align-items:center}
.hero-pager span{width:9px;height:9px;border-radius:50%;background:#111}
.hero-pager span.on{background:var(--white)}

.support-tab{position:absolute;left:0;top:390px;width:44px;height:127px;background:linear-gradient(90deg,#d8d8d8,#f4f4f4);border:1px solid #bbb;border-left:none;border-radius:0 6px 6px 0;display:flex;align-items:center;justify-content:center}
.support-tab p{transform:rotate(-90deg);white-space:nowrap;font-size:10px;color:#555;line-height:12px;text-align:center}
.support-tab b{display:block;color:#333}

.content{position:absolute;left:90px;top:407px;width:718px;height:714px;background:var(--panel)}
.follow{position:absolute;right:8px;top:18px;display:flex;align-items:center;gap:4px;font-size:11px;color:var(--ink)}
.follow span.label{margin-right:4px}
.social{width:24px;height:24px;border-radius:4px;background:linear-gradient(#ececec,#c9c9c9);border:1px solid #b5b5b5}

.page-title{position:absolute;left:11px;top:58px;width:517px;font-family:"Philosopher",sans-serif;font-size:20.5px;line-height:25px;color:var(--ink);font-weight:400;border-bottom:1px solid #ddd;padding-bottom:8px}
.intro-photo{position:absolute;left:11px;top:132px;width:176px;height:175px;border:1px solid #bbb;padding:4px;background:var(--white)}
.intro-photo div{width:100%;height:100%;background:linear-gradient(#5a3a22,#3a2a1e 55%,#8a6a4a)}
.intro{position:absolute;left:11px;top:128px;width:517px;font-size:11px;line-height:15.5px;color:var(--text)}
.intro p{margin-bottom:8px}
.intro .wrap{margin-left:186px}

.section-title{position:absolute;left:11px;font-family:"Philosopher",sans-serif;font-size:19px;color:var(--ink);font-weight:400}
.areas-title{top:392px}
.areas{position:absolute;left:11px;top:429px;width:526px;height:44px;background:#e6e6e6;display:flex;align-items:center;gap:0;padding-left:10px;font-size:12.5px;color:#333}
.areas li{list-style:none;display:flex;align-items:center;gap:6px;width:146px}
.areas li::before{content:"›";width:13px;height:13px;border-radius:50%;background:var(--gold-light);color:#6a3b00;font-size:12px;line-height:11px;text-align:center;font-weight:700}

.cases-title{top:509px;width:517px;border-bottom:1px solid #ddd;padding-bottom:4px}
.case{position:absolute;top:546px;width:200px;display:flex;gap:8px}
.case-thumb{width:42px;height:42px;flex:none;background:linear-gradient(135deg,#f3b45a,#a4561c);border:1px solid #ccc}
.case p{font-size:10px;line-height:14px;color:#333}
.case small{display:block;font-family:"Roboto Slab",serif;font-style:italic;font-size:8px;color:#555;margin-top:2px}
.case small b{font-style:normal}

.payments{position:absolute;left:97px;top:625px;width:417px;height:78px;background:var(--white);border:1px solid #ddd;text-align:center;font-family:"Roboto Slab",serif;font-size:11.5px;line-height:18px;color:#7a4a2a;padding-top:7px}
.payment-row{display:flex;justify-content:center;gap:10px;margin-top:5px}
.payment-row span{width:32px;height:20px;border-radius:2px;background:#d6d6d6}

.sidebar{position:absolute;left:550px;top:61px;width:162px;height:643px;background:#e4e4e4;border:1px solid #c8c8c8}
.sidebar h2{position:absolute;left:8px;top:4px;font-family:"Philosopher",sans-serif;font-weight:700;font-size:17px;line-height:20px;color:var(--ink)}
.sidebar-art{position:absolute;left:0;top:48px;width:160px;height:110px;background:linear-gradient(#e4e4e4,#b58c5a 55%,#7a5632)}
.sidebar-note{position:absolute;left:7px;top:163px;width:150px;font-size:9.5px;line-height:13px;color:#222}
.field{position:absolute;left:7px;width:147px}
.field label{display:block;font-size:9.5px;color:#222;margin-bottom:4px}
.field .box{height:23px;background:var(--white);border:1px solid #c4c4c4}
.field .select{background:#ececec;position:relative}
.field .select::after{content:"";position:absolute;right:8px;top:9px;border:4px solid transparent;border-top:5px solid #777}
.field .area{height:110px}
.send{position:absolute;right:8px;top:538px;width:50px;height:22px;background:linear-gradient(var(--gold-light),var(--gold-dark));border:1px solid #9a5d10;font-family:"Roboto Slab",serif;font-weight:700;font-size:11px;color:#3a2000;display:flex;align-items:center;justify-content:center}

.footer-nav{position:absolute;left:90px;top:1121px;width:720px;height:34px;background:var(--footer-bar);display:flex;justify-content:space-between;align-items:center;padding:0 10px;font-size:10px;color:#e8e8e8}
.footer-nav i{font-style:normal;color:#aaa}
.site-footer{position:absolute;left:0;top:1134px;width:892px;height:66px;background:var(--black);z-index:-0}
.copyright{position:absolute;left:0;top:1162px;width:892px;text-align:center;font-size:9.5px;line-height:13px;color:#ddd}
</style>
</head>
<body>
<header class="site-header">
  <div class="brand"><span class="brand-mark"></span><span class="brand-name">Vendrick Legal</span></div>
  <div class="contact-block">
    <div class="contact-call">Call for a free evaluation of your case</div>
    <div class="contact-phone">Phone:&nbsp; 0491 - 302 - 778</div>
    <div class="contact-email">EMAIL US</div>
  </div>
  <nav class="main-nav">
    <span class="current">Home</span><span>About Us</span><span>Practice Areas</span><span>Scope Of Advice</span><span class="active">Legal Costs</span><span>Press</span><span>Recent Cases</span><span>FAQ</span><span>Links</span><span>Contact</span><span>Service Policy</span>
  </nav>
</header>

<div class="hero-band"></div>
<section class="hero" role="img" aria-label="Golden scales of justice and a wooden gavel before shelves of law books">
  <h1 class="hero-title">Know Your Rights !</h1>
  <p class="hero-copy">We provide easy-to-understand advice and expert assistance to help you navigate complex court procedures</p>
  <div class="hero-button">Free Consultation</div>
</section>
<div class="hero-pager"><span class="on"></span><span></span><span></span><span></span></div>

<div class="support-tab"><p>Free Support<b>OFFLINE</b></p></div>

<main class="content">
  <div class="follow"><span class="label">Folow Us On :</span>
    <span class="social" title="Chatterloom"></span><span class="social" title="Quibbr"></span><span class="social" title="WorkMesh"></span><span class="social" title="Zumbly+"></span>
  </div>

  <h2 class="page-title">Criminal Defence Lawyer, Traffic Defence Lawyer &amp; Civil Litigation Lawyer, Perth WA</h2>

  <div class="intro-photo"><div role="img" aria-label="Two people shaking hands in front of law books"></div></div>
  <div class="intro">
    <div class="wrap">
      <p>Vendrick Legal is an established <a>law firm</a> practicing in Criminal Law, Traffic Law and Civil Law. We are <a>conveniently located</a> close to the Perth Magistrates Court and District Court.</p>
      <p>We understand that facing legal proceedings is very daunting and our clients are always saying "we don't know what to expect, we haven't been through anything like this before".</p>
      <p>We provide easy-to-understand advice and expert assistance to help you navigate complex <a>court</a> procedures. Our legal fees are open and transparent so you know from day one how much your <a>legal defence</a> is going to cost. We service all metropolitan courts as well as providing a visiting service to Karratha and Port Hedland.</p>
    </div>
    <p>Our office hours are 8:30 - 5:00 pm <a>Monday to Friday</a> but appointments can be made outside of these times.</p>
    <p>CALL Dorian NOW for an obligation <a>FREE assessment</a> of your case on 0491 302 778 or email us.</p>
  </div>

  <h2 class="section-title areas-title">Areas Of Practice &amp; Legal Services</h2>
  <ul class="areas"><li>Criminal Law</li><li>Traffic Law</li><li>Civil Law</li></ul>

  <h2 class="section-title cases-title">Read “Recent Cases” :</h2>
  <article class="case" style="left:9px">
    <div class="case-thumb" role="img" aria-label="Gavel thumbnail"></div>
    <p>Vestibulum a eros tellus, quis adipiscing neque. Sed varius, risus<small>March 14 2011, <b>42 Comments</b></small></p>
  </article>
  <article class="case" style="left:311px">
    <div class="case-thumb" role="img" aria-label="Gavel thumbnail"></div>
    <p>Vestibulum a eros tellus, quis adipiscing neque. Sed varius, risus<small>March 14 2011, <b>42 Comments</b></small></p>
  </article>

  <div class="payments">
    For your convenience we accept Paylink , CardMark and Vantapay.<br>Other major credit cards accepted
    <div class="payment-row"><span></span><span></span><span></span></div>
  </div>

  <aside class="sidebar">
    <h2>Free<br>Consultation</h2>
    <div class="sidebar-art" role="img" aria-label="Open law books with a small set of scales"></div>
    <p class="sidebar-note">Integer a sapien id diam temore unt Ut cursus nisl vel orci tristiqu eros</p>
    <div class="field" style="top:198px"><label>*Name :</label><div class="box"></div></div>
    <div class="field" style="top:241px"><label>*Phone Number :</label><div class="box"></div></div>
    <div class="field" style="top:285px"><label>*Email Addres :</label><div class="box"></div></div>
    <div class="field" style="top:333px"><label>*Consultation In :</label><div class="box select"></div></div>
    <div class="field" style="top:381px"><label>*Questions and comments :</label><div class="box area"></div></div>
    <div class="send">Send</div>
  </aside>
</main>

<footer>
  <div class="site-footer"></div>
  <nav class="footer-nav">
    <span>Home</span><i>|</i><span>About Us</span><i>|</i><span>Practice Areas</span><i>|</i><span>Scope Of Advice</span><i>|</i><span>Legal Costs</span><i>|</i><span>Press</span><i>|</i><span>FAQ</span><i>|</i><span>Recent Cases</span><i>|</i><span>Links</span><i>|</i><span>Contact</span><i>|</i><span>Service Policy</span>
  </nav>
  <div class="copyright">Copyright © 2013 Vendrick Legal<br>Website By: Brightnook Studio</div>
</footer>
</body>
</html>
```